A4 Block Hour Agreement Brochure

We need a new Block Hour Agreement Brochure created as our current one lacks design and is ugly. The current block hour agreement brochure has been attached "briefnook.pdf".

We are looking at a modern brochure and have attached "Pellamont Private Cloud Plans.pdf" as an example.

It doesnt have to be the exact same design, but it must be the "Pellamont blue" theme.

Target Market(s)

Information Technology

Colors
0054AA
0677BA
7BADD7
CADEEF
E8F1F8

```html
<!DOCTYPE html>
<html lang="en">
<head>
<meta charset="utf-8">
<title>Pellamont Block Hour Agreement</title>
<link rel="stylesheet" href="https://fonts.googleapis.com/css2?family=Cabin:wght@400;600&family=Kanit:wght@600&display=swap">
<style>
  :root {
    --navy: #28215f;
    --navy-mid: #2b3a8c;
    --brand-blue: #0054AA;
    --brand-bright: #0677BA;
    --brand-light: #7BADD7;
    --brand-pale: #CADEEF;
    --brand-mist: #E8F1F8;
    --grey: #b9bcc2;
    --backdrop: #e7e7e7;
    --white: #ffffff;
  }
  * { margin: 0; padding: 0; box-sizing: border-box; }
  html, body { width: 1200px; height: 792px; overflow: hidden; background: var(--backdrop); }
  .canvas { position: relative; width: 1200px; height: 792px; }
  .page {
    position: absolute; left: 320px; top: 0; width: 560px; height: 792px;
    background: var(--white); overflow: hidden;
    font-family: "Cabin", sans-serif; color: var(--white);
  }
  .page-art { position: absolute; inset: 0; }
  .brand {
    position: absolute; left: 36px; top: 30px; display: flex; align-items: center; gap: 10px;
    font-family: "Cabin", sans-serif; font-weight: 600; font-size: 22px; color: var(--navy);
    letter-spacing: 1px;
  }
  .brand-square { width: 22px; height: 22px; background: var(--brand-blue); }
  .title {
    position: absolute; left: 0; right: 0; top: 112px; text-align: center;
    font-family: "Kanit", sans-serif; font-weight: 600; font-size: 25px; letter-spacing: 1px;
  }
  .content { position: absolute; left: 40px; top: 165px; width: 400px; font-size: 9.6px; line-height: 1.35; }
  .content h2 { font-weight: 400; font-size: 11px; margin-bottom: 4px; }
  .content p { margin-bottom: 10px; color: var(--brand-mist); }
  .terms { list-style: none; color: var(--brand-mist); }
  .terms li::before { content: "• "; }
  .after-hours { color: var(--brand-mist); margin-top: 1px; }
  .rates {
    position: absolute; left: 56px; top: 470px; width: 300px; border-collapse: collapse;
    font-size: 11px; color: var(--white); background: rgba(0, 84, 170, 0.28);
  }
  .rates th, .rates td { border: 1px solid var(--brand-pale); padding: 4px 8px; text-align: center; font-weight: 400; }
  .rates .caption-row th { font-weight: 600; font-size: 12px; }
  .footer-note {
    position: absolute; left: 48px; top: 742px; width: 420px;
    font-size: 8.4px; line-height: 1.35; color: var(--navy);
  }
</style>
</head>
<body>
<div class="canvas">
  <article class="page">
    <svg class="page-art" width="560" height="792" viewBox="0 0 560 792">
      <defs>
        <linearGradient id="panelFill" x1="0" y1="1" x2="1" y2="0">
          <stop offset="0" stop-color="#28215f"/>
          <stop offset="0.55" stop-color="#2b3a8c"/>
          <stop offset="1" stop-color="#0677BA"/>
        </linearGradient>
        <linearGradient id="serverFill" x1="0" y1="0" x2="1" y2="1">
          <stop offset="0" stop-color="#CADEEF"/>
          <stop offset="0.45" stop-color="#3c5f8f"/>
          <stop offset="1" stop-color="#1b2b4d"/>
        </linearGradient>
        <linearGradient id="wedgeFill" x1="0" y1="0" x2="0" y2="1">
          <stop offset="0" stop-color="#0677BA"/>
          <stop offset="1" stop-color="#2b3a8c"/>
        </linearGradient>
      </defs>
      <rect class="blue-panel" x="0" y="88" width="560" height="632" fill="url(#panelFill)"/>
      <polygon class="header-notch" points="0,88 200,88 150,120 0,120" fill="#ffffff"/>
      <polygon class="server-photo" role="img" aria-label="Photo of server racks in a data centre" points="470,300 560,300 560,640 420,700" fill="url(#serverFill)"/>
      <polygon class="accent-wedge" points="510,420 560,400 560,650 500,680" fill="url(#wedgeFill)"/>
      <polygon class="grey-strip" points="440,720 560,630 560,660 480,720" fill="#b9bcc2"/>
      <rect class="footer-rule" x="0" y="786" width="560" height="6" fill="#28215f"/>
      <line x1="0" y1="780" x2="560" y2="780" stroke="#0677BA" stroke-width="2"/>
    </svg>

    <div class="brand"><span class="brand-square"></span><span>PELLAMONT</span></div>

    <h1 class="title">Block Hour Agreement</h1>

    <section class="content">
      <h2>Overview</h2>
      <p>Pellamont Technologies offers the Block Time Service Agreement at a discounted hourly rate for clients who need consistent support throughout a period of time. A block time agreement lets you pre-pay for services and call upon them as needed, this allows for easy accounting and easy support.</p>
      <p>Our Block Time Service Agreement can be used for all non-project related work. Please ask your Pellamont representative for more details.</p>
      <p>Block hours are not covered under a Service Level Agreement (SLA) and are best effort, while we endeavor to always provide prompt service to our customers in some situations such as a service disruption, it may not always be possible to attend straight away.</p>
      <ul class="terms">
        <li>Block hours do not rollover</li>
        <li>There is no set usage per week.</li>
        <li>Project services cannot be used with block time.</li>
        <li>Time is billed in 0.5 hour increments with a minimum of 1 hour for onsite callouts.</li>
        <li>Time must be used within 12 months of purchase</li>
        <li>Hours must be used during standard business hours 8:30am-5pm AWST.</li>
        <li>Hours must be used during standard business hours 8:30am-5pm AWST.</li>
      </ul>
      <div class="after-hours">After hours is charged at double time</div>
    </section>

    <table class="rates">
      <tr class="caption-row"><th colspan="3">Agreement Types</th></tr>
      <tr><th>Hours</th><th>Hourly Rate</th><th>Cost (Ex GST)</th></tr>
      <tr><td>1</td><td>$270.00</td><td>$265.00</td></tr>
      <tr><td>10</td><td>$240.00</td><td>$2,400.00</td></tr>
      <tr><td>20</td><td>$225.00</td><td>$4,500.00</td></tr>
      <tr><td>35</td><td>$220.00</td><td>$7,700.00</td></tr>
      <tr><td>50</td><td>$210.00</td><td>$10,500.00</td></tr>
    </table>

    <p class="footer-note">By engaging with Pellamont in goods/services you agree to our Terms and Conditions available at https://www.pellamonttech.com.au/terms</p>
  </article>
</div>
</body>
</html>
```